Private practice for psychiatry and psychotherapy needs a business card and logo

I need a logo and business card design for my private practice for psychiatry and psychotherapy. The optional names for my practice are: Voskuilen Praktijk voor Psychiatrie en Psychotherapie, or short: Praktijk Voskuilen.
I am a (child and adolescent) psychiatrist and psychotherapist. I diagnose and treat infants, children, adolescents and adults with psychiatric symptoms/disorders. I also give supervision to colleagues about their own treatments. My work is characterised by personal involvement, transparence, creativity and professionality.
I would like to have an appealing, light and bright, yet basic design that invites people (both children and adults) to contact me, gives trust and hope, without loosing professional appearance.
I uploaded my contact information which should not necessarily be all included (in this form) on the card as long as people know how to contact me. Please feel free to be creative!
Please note that my website is only temporarely and need a new design and update too!

Target Market(s)

Clients and patients (children, adolescents, adults) with psychiatric symptoms who need diagnosis and treatment. I work with private clients and patients through medical insurances.

Industry/Entity Type

Mental Health

Contact Information for Business Card

Dr. Femke Voskuilen-ter Horst
Psychiater/Kinder- en Jeugdpsychiater
Gerrit Wassinkstraat 4
3063 TW Rotterdam
t: 06-58190274
e: info@praktijkvoskuilen-voorbeeld.nl
i: www.praktijkvoskuilen-voorbeeld.nl

Logo Text

Praktijk Voskuilen voor Psychiatrie en Psychotherapie; or short: Praktijk Voskuilen

Font styles to use
Sans Serif
Other font styles liked:
• up to designer

Requirements
Must have
• Appealing, light, bright, creative, trustful, professional and unique.

```html
<!DOCTYPE html>
<html lang="nl">
<head>
<meta charset="utf-8">
<title>Praktijk Voskuilen – visitekaartje</title>
<link rel="stylesheet" href="https://fonts.googleapis.com/css2?family=Open+Sans:wght@400;600;700&display=swap">
<style>
  :root {
    --backdrop: #d9d9d9;
    --card: #f3f3f1;
    --ink: #1c1c1c;
    --brand-blue: #1f6db5;
    --brand-red: #d22a55;
  }
  * { box-sizing: border-box; margin: 0; padding: 0; }
  html, body {
    width: 1200px; height: 799px; overflow: hidden;
    background: var(--backdrop);
    font-family: "Open Sans", Arial, sans-serif;
    color: var(--ink);
  }
  .canvas { position: relative; width: 1200px; height: 799px; }
  .card {
    position: absolute; width: 520px; height: 315px;
    background: var(--card);
    box-shadow: 0 6px 18px rgba(0,0,0,0.12);
  }

  /* Front card */
  .card--front { left: 60px; top: 400px; }
  .services {
    position: absolute; right: 40px; top: 34px;
    list-style: none; text-align: right;
    font-size: 13px; line-height: 17px; letter-spacing: 0.5px;
    text-transform: uppercase;
  }
  .wordmark {
    position: absolute; left: 40px; bottom: 42px;
    display: flex; align-items: center; gap: 16px;
  }
  .wordmark__square { width: 28px; height: 28px; background: var(--brand-red); }
  .wordmark__name {
    font-size: 34px; font-weight: 400; letter-spacing: 1.5px;
    text-transform: uppercase; color: var(--ink);
  }

  /* Back card */
  .card--back { left: 620px; top: 90px; }
  .identity { position: absolute; left: 0; top: 92px; display: flex; gap: 12px; }
  .identity__square { width: 40px; height: 40px; background: var(--brand-red); }
  .identity__name {
    font-size: 17px; font-weight: 700; color: var(--brand-blue);
    text-transform: uppercase; line-height: 21px;
  }
  .identity__title {
    font-size: 14px; font-weight: 400; text-transform: uppercase; line-height: 18px;
  }
  .address {
    position: absolute; left: 24px; top: 160px;
    font-style: normal; font-size: 15px; line-height: 19px;
  }
  .web {
    position: absolute; right: 24px; bottom: 28px;
    font-size: 14px; line-height: 19px; text-align: left;
  }
</style>
</head>
<body>
<main class="canvas">
  <section class="card card--front" aria-label="Voorkant visitekaartje">
    <ul class="services">
      <li>Psychiatrie</li>
      <li>Psychotherapie</li>
      <li>Leertherapie</li>
      <li>Supervisie</li>
      <li>Coaching</li>
    </ul>
    <div class="wordmark">
      <span class="wordmark__square" aria-hidden="true"></span>
      <span class="wordmark__name">Praktijk Voskuilen</span>
    </div>
  </section>

  <section class="card card--back" aria-label="Achterkant visitekaartje">
    <div class="identity">
      <span class="identity__square" aria-hidden="true"></span>
      <div>
        <p class="identity__name">Dr. Femke Voskuilen-ter Horst</p>
        <p class="identity__title">Psychiater/Kinder- en Jeugdpsychiater</p>
      </div>
    </div>
    <address class="address">
      Gerrit Wassinkstraat 4<br>
      3063 TW&nbsp; Rotterdam<br>
      06-58190274
    </address>
    <p class="web">
      info@praktijkvoskuilen-voorbeeld.nl<br>
      www.praktijkvoskuilen-voorbeeld.nl
    </p>
  </section>
</main>
</body>
</html>
```